Business letterhead and powerpoint template

Hi, I have recently started using a new logo (found through PixelGrove) and would now like to use that logo for letterheads and powerpoint.

Attached is the logo and one version of a brochure I have recently used.

Industry/Entity Type

Business

```html
<!DOCTYPE html>
<html lang="en">
<head>
<meta charset="utf-8">
<title>Halden Capital Letterhead</title>
<link href="https://fonts.googleapis.com/css2?family=Quicksand:wght@400;500;600&display=swap" rel="stylesheet">
<style>
  :root {
    --backdrop: #e9e9eb;
    --paper: #ffffff;
    --ink: #3a3a3a;
    --ink-soft: #5a5a5a;
    --accent: #d9533a;
  }
  * { margin: 0; padding: 0; box-sizing: border-box; }
  html, body { width: 1200px; height: 960px; overflow: hidden; }
  body {
    background: var(--backdrop);
    font-family: "Quicksand", sans-serif;
    color: var(--ink);
    position: relative;
  }
  .letterhead {
    position: absolute;
    left: 282px; top: 30px;
    width: 636px; height: 900px;
    background: var(--paper);
    box-shadow: 0 2px 10px rgba(0,0,0,0.08);
    overflow: hidden;
  }
  .brand {
    position: absolute;
    left: 0; right: 0; top: 78px;
    display: flex; justify-content: center; align-items: center; gap: 10px;
  }
  .brand-mark { width: 14px; height: 14px; background: var(--accent); }
  .brand-name {
    font-size: 24px; font-weight: 500; letter-spacing: 2px;
    color: var(--ink); text-transform: uppercase;
  }
  .brand-rule {
    position: absolute; left: 232px; right: 232px; top: 116px;
    height: 1px; background: var(--ink-soft);
  }
  .date {
    position: absolute; right: 60px; top: 70px;
    font-size: 10px; color: var(--ink);
  }
  .letter {
    position: absolute; left: 60px; top: 196px; width: 430px;
  }
  .salutation { font-size: 11px; font-weight: 500; margin-bottom: 18px; }
  .body-copy { font-size: 9.5px; line-height: 1.7; color: var(--ink-soft); }
  .body-copy p + p { margin-top: 20px; }
  .accent-block {
    position: absolute; right: 0; top: 470px;
    width: 110px; height: 110px; background: var(--accent);
  }
  .sign-off {
    margin-top: 30px; margin-left: 150px;
    font-size: 11px; color: var(--ink);
  }
  .sign-off .company { margin-top: 22px; text-transform: uppercase; letter-spacing: 0.5px; }
  .contact {
    position: absolute; left: 210px; bottom: 32px;
    font-size: 10px; line-height: 1.55; color: var(--ink); font-style: normal;
  }
  .contact .company-name { color: var(--accent); text-transform: uppercase; font-weight: 500; }
  .contact-row { display: flex; gap: 8px; align-items: flex-start; }
  .contact-row svg { width: 10px; height: 10px; margin-top: 3px; flex: none; }
</style>
</head>
<body>
  <main class="letterhead">
    <div class="brand">
      <span class="brand-mark"></span>
      <span class="brand-name">Halden Capital</span>
    </div>
    <div class="brand-rule"></div>
    <div class="date">Date : 02-Aug-14</div>

    <div class="accent-block"></div>

    <section class="letter">
      <div class="salutation">Sir / Madam,</div>
      <div class="body-copy">
        <p>Lorem ipsum dolor sit amet, consectetur adipiscing elit. Aenean vel placerat nisi, id vestibulum tellus. Proin ligula ipsum, ultrices sit amet justo id, ullamcorper porttitor augue. Nulla sed metus ut nunc hendrerit porta. Sed egestas luctus cursus. Etiam commodo turpis nulla, sed ornare augue scelerisque vel. Aliquam erat volutpat. Nam scelerisque tincidunt risus a ultrices. Aenean imperdiet ante mi, vel dictum nibh tempor ac. Nunc auctor ut lorem vel vulputate. Praesent magna nunc, rhoncus ut ipsum eget, ullamcorper auctor nulla. Lorem ipsum dolor sit amet, consectetur adipiscing elit. Aenean vel placerat nisi, id vestibulum tellus. Proin ligula ipsum, ultrices sit amet justo id, ullamcorper porttitor augue. Nulla sed metus ut nunc hendrerit porta. Sed egestas luctus cursus. Etiam commodo turpis nulla, sed ornare augue scelerisque vel. Aliquam erat volutpat. Nam scelerisque tincidunt risus a ultrices. Aenean imperdiet ante mi, vel dictum nibh tempor ac. Nunc auctor ut lorem vel vulputate. Praesent magna nunc, rhoncus ut ipsum eget, ullamcorper auctor nulla.</p>
        <p>Phasellus sem justo, suscipit ac laoreet id, tincidunt vel mauris. Nullam vulputate nisi ut sodales pulvinar. Vivamus convallis fringilla arcu non pellentesque. Aenean sed commodo neque. Duis volutpat eleifend sapien, et aliquam quam facilisis eu. Suspendisse viverra nec ligula quis scelerisque. Etiam nibh magna, aliquet vel aliquam quis, fermentum vestibulum nulla. Fusce pellentesque, sem vel tristique pretium, risus elit sodales lectus, non aliquet nunc ipsum et nulla. Nunc sapien neque, pulvinar vel suscipit quis, laoreet non sapien. Phasellus sem justo, suscipit ac laoreet id, tincidunt vel mauris. Nullam vulputate nisi ut sodales pulvinar. Vivamus convallis fringilla arcu non pellentesque. Aenean sed commodo neque. Duis volutpat eleifend sapien, et aliquam quam facilisis eu. Suspendisse viverra nec ligula quis scelerisque. Etiam nibh magna, aliquet vel aliquam quis, fermentum vestibulum nulla. Fusce pellentesque, sem vel tristique pretium, risus elit sodales lectus, non aliquet nunc ipsum et nulla. Nunc sapien neque, pulvinar vel suscipit quis, laoreet non sapien.</p>
      </div>
      <div class="sign-off">
        <div>Yours Sincerely</div>
        <div class="company">Halden Capital</div>
      </div>
    </section>

    <address class="contact">
      <div class="company-name">Halden Capital</div>
      <div class="contact-row">
        <svg viewBox="0 0 10 10"><path d="M5 0.5a3.2 3.2 0 0 0-3.2 3.2C1.8 6 5 9.5 5 9.5S8.2 6 8.2 3.7A3.2 3.2 0 0 0 5 0.5z" fill="var(--accent)"/><circle cx="5" cy="3.7" r="1.1" fill="#fff"/></svg>
        <div>Level 8 Suite 14<br>42 Harbour Lane<br>Eastwood 3100 VIC<br>Australia</div>
      </div>
      <div class="contact-row">
        <svg viewBox="0 0 10 10"><rect x="2" y="0.5" width="6" height="9" rx="1.2" fill="var(--accent)"/><rect x="3" y="1.8" width="4" height="5.5" fill="#fff"/></svg>
        <div>Phone: +61 (0)3 5550 1420</div>
      </div>
      <div class="contact-row">
        <svg viewBox="0 0 10 10"><rect x="0.5" y="3" width="9" height="5.5" rx="1" fill="var(--accent)"/><rect x="2.5" y="0.8" width="5" height="3" fill="none" stroke="var(--accent)"/></svg>
        <div>Fax: &nbsp;+61 (0)3 5550 1421</div>
      </div>
      <div class="contact-row">
        <svg viewBox="0 0 10 10"><circle cx="5" cy="5" r="4.3" fill="none" stroke="var(--accent)" stroke-width="1.2"/><path d="M0.7 5h8.6M5 0.7c-2 2.5-2 6.1 0 8.6M5 0.7c2 2.5 2 6.1 0 8.6" fill="none" stroke="var(--accent)" stroke-width="0.8"/></svg>
        <div>www.haldencapital.example</div>
      </div>
    </address>
  </main>
</body>
</html>
```